Tech Company requires UI design for mobile app

We need a mobile app design for a company based in Singapore called "Kalvor Systems". We develop innovative Android/iOS business applications. KalvorLink - a collaboration tool targeted at SMEs that improves reporting and communication between different departments of an organisation. We would like to see designs that use the colour orange, our corporate colour. The final design should communicate clean and technology inclined design.

You are expected to recreate the icons, layout and structure without affecting the workflow.This is a workplace app for employee on mobile. The mobile app aims to empower individual employee to complete the following processes:

1. HR processes - taking attendance, timesheet, employment management to payslip)
2. Inventory management - stock taking, gift redemption and real-time stock management
3. Digital form - application for inspection, safety, procurement or request creation)
4. Job - an app that allows web portal to assign work to individual worker.
Updates

Reason: Received feedback to extens timeline. Cheers!

Target Market(s)

C-Executive, office employee, retail promoter, worker

Industry/Entity Type

Business

Colors

Designer to choose colors to be used in the design.

Requirements
Must have
• - Design must be neat, looks professional and perceived to be user-friendly
• - Use colour theme for each category
• - Must complement with KalvorLink logo them (already attached)
• - Have "apple" feel
• - We like the layout reference 1 & reference 2 photo. However, we prefer a better colour theme (Already Attached)
• - Please download the link for the work required
• https://files.quillbox.example/open?id=7Hq2LmPzXw9RtNc4VbKjYs8DfGaTe3Uo
Nice to have
• More info to follow shortly
Should not have
• - Must not be loud, flashy, dull, bored,
• - Design should not clash with Kalvor Link Logo
• -

```html
<!DOCTYPE html>
<html lang="en">
<head>
<meta charset="utf-8">
<title>Kalvor Link — App Screens</title>
<link href="https://fonts.googleapis.com/css2?family=Poppins:wght@300;400;500;600&family=Quicksand:wght@300;400;500&display=swap" rel="stylesheet">
<style>
:root{
  --board:#232323;
  --orange:#f27224;
  --orange-deep:#e85f1a;
  --white:#ffffff;
  --ink:#333333;
  --muted:#7a7a7a;
  --line:#e6e6e6;
  --green:#41e084;
  --red:#f25a4f;
  --link:#1e9be8;
  --cam-dark:#3a3a3a;
}
*{box-sizing:border-box;margin:0;padding:0}
html,body{width:1200px;height:1200px;overflow:hidden;background:var(--board)}
body{position:relative;font-family:"Poppins",sans-serif;color:var(--ink)}

.brand-title{position:absolute;left:232px;top:44px;display:flex;align-items:center;gap:18px}
.brand-title .dot{width:40px;height:40px;border-radius:50%;background:var(--white)}
.brand-title span{font-family:"Quicksand",sans-serif;font-weight:300;font-size:78px;line-height:1;color:var(--white);letter-spacing:1px}

.caption{position:absolute;color:var(--white);font-weight:500;font-size:24px;line-height:1;white-space:nowrap}
.rule{position:absolute;height:2px;background:var(--white)}
.vrule{position:absolute;width:2px;background:var(--white)}

.screen{position:absolute;width:233px;height:413px;overflow:hidden;background:var(--white)}
.status{position:absolute;left:0;top:0;width:100%;height:14px;display:flex;align-items:center;justify-content:space-between;padding:0 6px;font-size:6.5px;color:#333}
.status .sig{letter-spacing:-1px;font-size:6px}
.status .bat{width:13px;height:5px;background:currentColor;border-radius:1px}
.status.light{color:var(--white)}

/* splash */
.splash-logo{position:absolute;left:0;right:0;text-align:center;font-family:"Quicksand",sans-serif;font-weight:400}
.splash-white .splash-logo{top:188px;font-size:28px;color:var(--ink);display:flex;justify-content:center;align-items:center;gap:8px}
.splash-white .splash-logo i{width:14px;height:14px;border-radius:50%;background:var(--orange)}
.splash-orange{background:var(--orange)}
.splash-orange .splash-logo{top:188px;font-size:28px;color:var(--white)}
.loading{position:absolute;top:260px;left:0;right:0;text-align:center;font-size:9px;color:var(--white)}

/* main screen */
.main{left:871px;top:81px;width:286px;height:576px}
.main-head{position:absolute;top:14px;left:0;right:0;height:28px;display:flex;align-items:center;justify-content:space-between;padding:0 14px}
.main-head .name{font-family:"Quicksand",sans-serif;font-size:13px;color:var(--ink);display:flex;align-items:center;gap:4px}
.main-head .name i{width:7px;height:7px;border-radius:50%;background:var(--orange)}
.quick-band{position:absolute;top:42px;left:0;right:0;height:109px;background:linear-gradient(var(--orange),var(--orange-deep))}
.quick{position:absolute;top:8px;left:0;right:0;display:grid;grid-template-columns:repeat(4,1fr);text-align:center;color:var(--white);font-size:6.5px;line-height:1.35}
.quick svg{display:block;margin:0 auto 5px;width:28px;height:28px}
.profile-card{position:absolute;left:14px;top:118px;width:258px;height:63px;background:var(--white);border-radius:3px;box-shadow:0 2px 6px rgba(0,0,0,.15);display:flex;align-items:center;padding-left:17px;gap:13px}
.avatar{border-radius:50%;background:radial-gradient(circle at 50% 40%,#e8d6cc,#9b7c6c);border:2px solid var(--orange);flex:none}
.profile-card .avatar{width:40px;height:40px}
.profile-card .who{font-size:11px;line-height:1.35;color:var(--ink)}
.online{position:absolute;width:7px;height:7px;border-radius:50%;background:var(--green)}
.section-title{position:absolute;left:15px;font-size:10px;font-weight:500;color:var(--ink)}
.tiles{position:absolute;left:0;right:0;display:grid;grid-template-columns:repeat(4,1fr);text-align:center;font-size:6.5px;line-height:1.3;color:var(--muted)}
.tiles svg{display:block;margin:0 auto 6px;width:26px;height:26px}
.ico{fill:none;stroke:#555;stroke-width:1.3;stroke-linecap:round;stroke-linejoin:round}
.ico-w{fill:none;stroke:var(--white);stroke-width:1.6;stroke-linecap:round;stroke-linejoin:round}
.tabbar{position:absolute;left:0;right:0;bottom:0;height:34px;border-top:1px solid var(--line);background:#fafafa;display:grid;grid-template-columns:repeat(4,1fr);text-align:center;font-size:6px;color:#999;padding-top:5px}
.tabbar svg{display:block;margin:0 auto 1px;width:18px;height:18px}
.tabbar .on{color:var(--orange)}

/* camera */
.camera{left:162px;top:699px;background:var(--cam-dark)}
.cam-top{position:absolute;top:14px;left:0;right:0;height:20px;display:flex;justify-content:center}
.cam-photo{position:absolute;top:34px;left:0;right:0;height:329px;background:radial-gradient(ellipse at 50% 40%,#8a6a4a,#3d2c1e 70%,#1e1610)}
.cam-bar{position:absolute;bottom:0;left:0;right:0;height:50px;display:flex;align-items:center;justify-content:space-between;padding:0 16px}
.shutter{width:40px;height:40px;border-radius:50%;background:var(--white);box-shadow:0 0 0 2px var(--cam-dark),0 0 0 3px var(--white)}

/* attendance */
.att-head{position:absolute;top:14px;left:0;right:0;height:20px;display:flex;align-items:center;justify-content:center;font-size:8.5px;color:var(--ink);letter-spacing:.3px}
.att-head .back{position:absolute;left:14px;top:5px}
.map{position:absolute;top:34px;left:0;right:0;height:287px;background:linear-gradient(160deg,#e6e2d8,#d8d4c8 55%,#cfd6c8)}
.att-band{position:absolute;top:34px;left:0;right:0;height:36px;background:var(--orange)}
.att-card{position:absolute;left:12px;top:54px;width:209px;height:77px;background:var(--white);border-radius:3px;box-shadow:0 2px 6px rgba(0,0,0,.15)}
.att-card .avatar{position:absolute;left:14px;top:12px;width:33px;height:33px}
.att-card .who{position:absolute;left:67px;top:10px;font-size:9px;line-height:1.35}
.att-card .addr{position:absolute;left:67px;top:37px;font-size:6px;line-height:1.35;color:#555;display:flex;gap:3px}
.att-card .when{position:absolute;right:8px;bottom:5px;font-size:5.5px;color:#555}
.att-foot{position:absolute;top:321px;left:0;right:0;bottom:0;background:var(--white)}
.att-meta{position:absolute;left:12px;top:11px;display:grid;grid-template-columns:64px auto;row-gap:3px;font-size:8.5px}
.att-meta dt{color:#999}
.att-meta .proj{color:var(--link)}
.btn{position:absolute;top:46px;width:93px;height:35px;border-radius:2px;color:var(--white);font-size:8.5px;display:flex;align-items:center;justify-content:center;gap:6px}
.btn.in{left:13px;background:var(--green)}
.btn.out{left:127px;background:var(--red)}
.scrim{position:absolute;inset:0;background:rgba(20,20,20,.72)}
.dialog{position:absolute;left:12px;top:109px;width:209px;height:178px;background:var(--white);border-radius:3px;overflow:hidden}
.dialog h3{height:34px;background:var(--orange);color:var(--white);font-weight:400;font-size:10px;display:flex;align-items:center;justify-content:center}
.dialog .d-ico{position:absolute;top:52px;left:0;right:0;display:flex;justify-content:center}
.dialog .d-sub{position:absolute;top:88px;left:0;right:0;text-align:center;font-size:10px;color:#aaa}
.dialog .d-main{position:absolute;top:106px;left:0;right:0;text-align:center;font-size:10px;color:var(--ink)}
.dialog .d-actions{position:absolute;left:0;right:0;bottom:0;height:39px;border-top:1px solid var(--line);display:flex;justify-content:space-around;align-items:center;font-size:10px;color:#888}
.dialog .d-actions .go{color:var(--orange);font-weight:500}
</style>
</head>
<body>

<div class="brand-title"><div class="dot"></div><span>Kalvor</span></div>

<!-- Splash -->
<div class="screen splash-white" style="left:162px;top:193px">
  <div class="status"><span class="sig">●●●●● ◠</span><span>9:00 AM</span><span class="bat"></span></div>
  <div class="splash-logo"><i></i>Kalvor</div>
</div>
<div class="screen splash-orange" style="left:410px;top:193px">
  <div class="status light"><span class="sig">●●●●● ◠</span><span>9:00 AM</span><span class="bat"></span></div>
  <div class="splash-logo">Kalvor</div>
  <div class="loading">Loading</div>
</div>
<div class="rule" style="left:162px;top:649px;width:176px"></div>
<div class="caption" style="left:365px;top:634px">Splash</div>
<div class="rule" style="left:462px;top:649px;width:176px"></div>

<!-- Main screen label -->
<div class="vrule" style="left:823px;top:80px;height:176px"></div>
<div class="caption" style="left:822px;top:368px;transform:translate(-50%,-50%) rotate(-90deg)">Main Screen</div>
<div class="vrule" style="left:823px;top:480px;height:176px"></div>

<!-- Main screen -->
<div class="screen main">
  <div class="status"><span class="sig">●●●●● ◠</span><span>9:00 AM</span><span class="bat"></span></div>
  <div class="main-head">
    <svg width="14" height="14" viewBox="0 0 14 14"><path d="M3 10V6a4 4 0 0 1 8 0v4l1 1H2z M6 12h2" fill="var(--orange)"/><circle cx="11" cy="2.5" r="1.6" fill="var(--green)"/></svg>
    <div class="name"><i></i>Kalvor</div>
    <svg width="14" height="14" viewBox="0 0 14 14"><circle cx="7" cy="7" r="4.3" fill="none" stroke="var(--orange)" stroke-width="3" stroke-dasharray="2.2 1.2"/><circle cx="7" cy="7" r="2.8" fill="var(--orange)"/><circle cx="7" cy="7" r="1.2" fill="#fff"/></svg>
  </div>
  <div class="quick-band">
    <div class="quick">
      <div><svg viewBox="0 0 28 28" class="ico-w"><path d="M11 20V9a2 2 0 0 1 4 0v6l5 1a2 2 0 0 1 1.5 2.4L20 25h-8l-4-5a1.6 1.6 0 0 1 2.5-2z"/><path d="M8 9a5 5 0 0 1 10 0"/></svg>Take<br>Attendance</div>
      <div><svg viewBox="0 0 28 28" class="ico-w"><circle cx="14" cy="14" r="11" fill="#fff3" /><circle cx="14" cy="14" r="8.5"/><path d="M14 9v5h4"/></svg>Today</div>
      <div><svg viewBox="0 0 28 28" class="ico-w"><rect x="4" y="7" width="13" height="17" rx="1"/><path d="M7 12h7M7 16h7M7 20h5"/><circle cx="20" cy="9" r="5.5"/><path d="M20 6.5V9h2"/></svg>Past<br>REcords</div>
      <div><svg viewBox="0 0 28 28" class="ico-w"><circle cx="10" cy="9" r="3.5" fill="#fff"/><circle cx="18" cy="9" r="3.5" fill="#fff"/><path d="M3 21a7 6 0 0 1 14 0zM11 21a7 6 0 0 1 14 0z" fill="#fff"/></svg>Station</div>
    </div>
  </div>
  <div class="profile-card">
    <div class="avatar" role="img" aria-label="Employee profile photo"></div>
    <div class="who">Mira Tolvanen<br>EM1254</div>
  </div>
  <div class="online" style="left:254px;top:127px"></div>

  <div class="section-title" style="top:199px">Sales</div>
  <div class="tiles" style="top:220px">
    <div><svg viewBox="0 0 26 26" class="ico"><rect x="4" y="10" width="18" height="13"/><rect x="3" y="7" width="20" height="4"/><path d="M13 7v16M13 7c-2-5-7-4-5 0M13 7c2-5 7-4 5 0"/></svg>New<br>Redemption</div>
    <div><svg viewBox="0 0 26 26" class="ico"><path d="M3 8l10-4 10 4-10 4zM3 8v10l10 4 10-4V8M13 12v10"/></svg>View<br>Redemption</div>
    <div><svg viewBox="0 0 26 26" class="ico"><path d="M3 9h5l2-3h6l2 3h5v13H3z"/><circle cx="13" cy="15" r="4.5"/></svg>Take<br>Photo</div>
    <div><svg viewBox="0 0 26 26" class="ico"><path d="M4 3v20h19"/><path d="M8 20v-6M12 20v-9M16 20v-5M20 20v-11M7 13l5-4 4 4 5-7"/></svg>Slaes<br>Summary</div>
  </div>

  <div class="section-title" style="top:288px">Inventory</div>
  <div class="tiles" style="top:309px">
    <div><svg viewBox="0 0 26 26" class="ico"><rect x="5" y="5" width="16" height="19" rx="1"/><rect x="9" y="3" width="8" height="4"/><path d="M8 12l2 2 3-3M8 18l2 2 3-3M15 13h3M15 19h3"/></svg>Inventory<br>Check</div>
    <div><svg viewBox="0 0 26 26" class="ico"><path d="M2 6h14v12H2zM16 10h5l3 4v4h-8"/><circle cx="6" cy="19" r="2"/><circle cx="19" cy="19" r="2"/></svg>Delivery</div>
    <div><svg viewBox="0 0 26 26" class="ico"><path d="M4 8l9-4 9 4-9 4zM4 8v10l9 4 9-4V8M13 12v10"/><circle cx="19" cy="19" r="3"/></svg>New<br>Stock Take</div>
    <div><svg viewBox="0 0 26 26" class="ico"><rect x="4" y="5" width="16" height="19" rx="1"/><path d="M8 10h8M8 14h8M8 18h8"/><path d="M21 4v18"/></svg>Stock<br>Take List</div>
  </div>

  <div class="section-title" style="top:377px">Leave</div>
  <div class="tiles" style="top:398px">
    <div><svg viewBox="0 0 26 26" class="ico"><path d="M4 11a9 6 0 0 1 18 0zM13 5v16M5 21h16M7 17h12"/></svg>Apply Leave</div>
    <div><svg viewBox="0 0 26 26" class="ico"><path d="M3 12a8 6 0 0 1 16 0zM11 6v15M3 21h16"/><path d="M22 3l-2 4h3l-2 4"/></svg>Leave Status</div>
    <div><svg viewBox="0 0 26 26" class="ico"><circle cx="16" cy="6" r="2.5"/><path d="M3 19l5-4h6a1.5 1.5 0 0 1 0 3h-4M8 22h9l6-6"/></svg>Balance</div>
    <div><svg viewBox="0 0 26 26" class="ico"><path d="M7 3h8M7 21h8M8 3c0 5 6 5 6 9s-6 4-6 9M14 3c0 3-2 4-3 5"/><circle cx="19" cy="17" r="4"/><path d="M19 15v2h2"/></svg>Pending Action</div>
  </div>

  <div class="section-title" style="top:459px">Workforce Management</div>
  <div class="tiles" style="top:480px">
    <div><svg viewBox="0 0 26 26" class="ico"><path d="M6 3h11l4 4v16H6z"/><path d="M9 9h8M9 13h8M9 17h8"/></svg>Forms</div>
    <div><svg viewBox="0 0 26 26" class="ico"><rect x="3" y="7" width="20" height="13"/><path d="M3 7l10 7 10-7"/></svg>My Jobs</div>
  </div>

  <div class="tabbar">
    <div class="on"><svg viewBox="0 0 18 18"><path d="M2 9l7-6 7 6h-2v7h-4v-4H8v4H4V9z" fill="var(--orange)"/></svg>Home</div>
    <div><svg viewBox="0 0 18 18"><circle cx="9" cy="5.5" r="3.5" fill="#999"/><path d="M2 17a7 6 0 0 1 14 0z" fill="#999"/></svg>Profile</div>
    <div><svg viewBox="0 0 18 18"><rect x="2" y="3" width="14" height="13" rx="1" fill="#999"/><path d="M4 7h10M4 10h10M4 13h10M7 7v7M11 7v7" stroke="#fafafa" stroke-width=".9"/></svg>Calendar</div>
    <div><svg viewBox="0 0 18 18"><path d="M4.5 14a3.5 3.5 0 0 1 0-7 5 5 0 0 1 9.5 1 3 3 0 0 1 0 6z" fill="#999"/><path d="M7 10a2 2 0 0 1 4 0M11 10l-1-1M7 11a2 2 0 0 0 4 0" fill="none" stroke="#fafafa" stroke-width="1"/></svg>Sunc</div>
  </div>
</div>

<!-- Camera -->
<div class="screen camera">
  <div class="status light"><span class="sig">●●●●● ◠</span><span>9:00 AM</span><span class="bat"></span></div>
  <div class="cam-top"><svg width="10" height="16" viewBox="0 0 10 16"><path d="M6 1L1 9h4l-1 6 5-8H5z" fill="#fff"/></svg></div>
  <div class="cam-photo" role="img" aria-label="Live camera preview of a worker holding a welding helmet"></div>
  <div class="cam-bar">
    <svg width="18" height="16" viewBox="0 0 18 16"><rect x="1" y="2" width="16" height="12" fill="none" stroke="#fff" stroke-width="1.5"/><path d="M3 12l4-5 3 3 2-2 3 4z" fill="#fff"/></svg>
    <div class="shutter"></div>
    <svg width="18" height="16" viewBox="0 0 18 16"><path d="M1 4h4l1.5-2h5L13 4h4v10H1z" fill="none" stroke="#fff" stroke-width="1.5"/><circle cx="9" cy="9" r="3" fill="none" stroke="#fff" stroke-width="1.5"/></svg>
  </div>
</div>
<div class="caption" style="left:280px;top:1134px;transform:translateX(-50%)">Camera</div>

<!-- Attendance: base view -->
<div class="screen" style="left:416px;top:699px">
  <div class="status"><span class="sig">●●●●● ◠</span><span>9:00 AM</span><span class="bat"></span></div>
  <div class="att-head"><svg class="back" width="8" height="10" viewBox="0 0 8 10"><path d="M6 1L2 5l4 4" fill="none" stroke="var(--orange)" stroke-width="1.8"/></svg>ATTENDANCE</div>
  <div class="map" role="img" aria-label="Street map showing the employee's clock-in location"></div>
  <div class="att-band"></div>
  <div class="att-card">
    <div class="avatar" role="img" aria-label="Employee profile photo"></div>
    <div class="who">Mira Tolvanen<br>EM1254</div>
    <div class="addr"><svg width="6" height="8" viewBox="0 0 6 8"><path d="M3 8L.6 4a2.6 2.6 0 1 1 4.8 0z" fill="var(--red)"/></svg><span>42 Harlow St. North Bexley,<br>CT 06190</span></div>
    <div class="when">14/10/2017 &nbsp; 08:12 AM</div>
    <div class="online" style="left:198px;top:7px;width:5px;height:5px"></div>
  </div>
  <div class="att-foot">
    <dl class="att-meta"><dt>Project</dt><dd class="proj">KTX-Office 118</dd><dt>Last Action</dt><dd>Clock in 14/10/2017 &nbsp;06:15pm</dd></dl>
    <div class="btn in"><svg width="14" height="14" viewBox="0 0 14 14"><path d="M2.5 7a4.5 4.5 0 1 0 1.3-3.2M1.5 2v2.5H4M7 4.5V7l2 1" fill="none" stroke="#fff" stroke-width="1.2"/></svg>CLOCK IN</div>
    <div class="btn out">CLOCK OUT<svg width="14" height="14" viewBox="0 0 14 14"><path d="M11.5 7a4.5 4.5 0 1 1-1.3-3.2M12.5 2v2.5H10M7 4.5V7l2 1" fill="none" stroke="#fff" stroke-width="1.2"/></svg></div>
  </div>
</div>

<!-- Attendance: confirm -->
<div class="screen" style="left:670px;top:699px">
  <div class="status"><span class="sig">●●●●● ◠</span><span>9:00 AM</span><span class="bat"></span></div>
  <div class="att-head">ATTENDANCE</div>
  <div class="map" role="img" aria-label="Street map showing the employee's clock-in location"></div>
  <div class="att-band"></div>
  <div class="att-card">
    <div class="avatar" role="img" aria-label="Employee profile photo"></div>
    <div class="who">Mira Tolvanen<br>EM1254</div>
  </div>
  <div class="att-foot">
    <dl class="att-meta"><dt>Project</dt><dd class="proj">KTX-Office 118</dd><dt>Last Action</dt><dd>Clock in 14/10/2017 &nbsp;06:15pm</dd></dl>
    <div class="btn in">CLOCK IN</div>
    <div class="btn out">CLOCK OUT</div>
  </div>
  <div class="scrim"></div>
  <div class="dialog">
    <h3>CONFIRM</h3>
    <div class="d-ico"><svg width="30" height="30" viewBox="0 0 30 30"><path d="M5 15a10 10 0 1 0 3-7.1M4 4v5h5M15 9v6l4 2" fill="none" stroke="#999" stroke-width="2"/></svg></div>
    <div class="d-sub">Check in for</div>
    <div class="d-main">EM1254 &nbsp;Mira Tolvanen</div>
    <div class="d-actions"><span>CANCEL</span><span class="go">OK</span></div>
  </div>
</div>

<!-- Attendance: sync success -->
<div class="screen" style="left:925px;top:699px">
  <div class="status"><span class="sig">●●●●● ◠</span><span>9:00 AM</span><span class="bat"></span></div>
  <div class="att-head">ATTENDANCE</div>
  <div class="map" role="img" aria-label="Street map showing the employee's clock-in location"></div>
  <div class="att-band"></div>
  <div class="att-card">
    <div class="avatar" role="img" aria-label="Employee profile photo"></div>
    <div class="who">Mira Tolvanen<br>EM1254</div>
  </div>
  <div class="att-foot">
    <dl class="att-meta"><dt>Project</dt><dd class="proj">KTX-Office 118</dd><dt>Last Action</dt><dd>Clock in 14/10/2017 &nbsp;06:15pm</dd></dl>
    <div class="btn in">CLOCK IN</div>
    <div class="btn out">CLOCK OUT</div>
  </div>
  <div class="scrim"></div>
  <div class="dialog">
    <h3>SYNC SUCCESS!</h3>
    <div class="d-ico"><svg width="34" height="28" viewBox="0 0 34 28"><path d="M9 24a7 7 0 0 1-.5-14A9.5 9.5 0 0 1 27 11a6.5 6.5 0 0 1-1 13z" fill="#999"/><path d="M17 24V13M12.5 17.5L17 13l4.5 4.5" fill="none" stroke="#fff" stroke-width="2.4"/></svg></div>
    <div class="d-sub">Attendance uploaded to server at</div>
    <div class="d-main">14/10/2017 07:15 pm</div>
    <div class="d-actions"><span class="go">HOME</span><span>TAKE ANOTHER</span></div>
  </div>
</div>

<div class="rule" style="left:416px;top:1146px;width:138px"></div>
<div class="caption" style="left:788px;top:1134px;transform:translateX(-50%)">Attendance View / Clock in clock out</div>
<div class="rule" style="left:1021px;top:1146px;width:137px"></div>

</body>
</html>
```